An expert for Professional and Technical Evaluation of Painting Work Needs a New Letterhead Design

I own a mid-sized painting company and also work as an expert for professional and technical evaluation of painting work in the area of Zurich.

Please read the project description and the must-have-requirements carefully!

I attached 1 PDF which will help you create a new letterhead design:

THE NEW DESIGN DOESN'T NEED A LOGO! (Because it won't represent a company, it represents only a service)
Updates

Dear designers We had a discussion about the location/placement of the design and came to the conclusion that we only want the design to be in the header area of the A4-paper. We would be glad to receive some revised version of your designs. Thank you and kind regards!

Project Deadline Extended
Reason: Due to the fact that only 20% of the designer have understood the brief and submitted designs that have met the requirements we decided to extend the contest deadline.

Project Deadline Extended
Reason: A great deal of good designs were submitted in the last few days. A big thank you to all the participating designers for your good work. We need a few more days to discuss some changes with certain designers and to decide which design will win.

Target Market(s)

(Insurance) Companies, partly also private clients.

Industry/Entity Type

Painting

Colors

Designer to choose colors to be used in the design.

Requirements
Must have
• All information (text, phone numbers, ...) of the old design ("old_letterhead_design.pdf") has also to be in the new one. Additional to that there are a few changes:
The phone numbers "01 583 61 47" and "01 583 61 37" change to "044 583 61 47" and "044 583 61 37". And please mention also this email address: gutachten@valmorkeller.example .

- The design should only be in the header-area of the A4-paper. An the background color of the A4-paper will be white.

- The design should consist of two designs. One for the first page and a smaller version of the design for the following pages.

- THE NEW DESIGN DOESN'T NEED A LOGO! You can make a design with geometric forms, ...

- The new design should have a juridical look. It should only contain colors like brown, fawn, black, light green, ...... colors which look serious/reliable.
Nice to have
• Geometric Forms, Symbols or other design elements.

- It would also be nice to have some design elements which emphasize the kind of work we are offering.

```html
<!DOCTYPE html>
<html lang="de">
<head>
<meta charset="utf-8">
<title>Valmor Keller – Briefpapier</title>
<link rel="stylesheet" href="https://fonts.googleapis.com/css2?family=Source+Sans+3:wght@400;600;700&display=swap">
<style>
  :root {
    --backdrop: #e8e6e3;
    --paper: #ffffff;
    --ink: #1c1c1c;
    --ink-soft: #3a3a3a;
    --facet-light: #f7f7f7;
    --facet-mid: #e4e4e4;
    --facet-deep: #d6d6d6;
    --sheet-shadow: rgba(0, 0, 0, 0.12);
  }
  * { box-sizing: border-box; margin: 0; padding: 0; }
  html, body { width: 1200px; height: 840px; overflow: hidden; background: var(--backdrop); }
  body { font-family: "Source Sans 3", "Myriad Pro", Arial, sans-serif; color: var(--ink); }
  .canvas { position: relative; width: 1200px; height: 840px; overflow: hidden; }

  .sheet { position: absolute; background: var(--paper); box-shadow: 0 6px 22px var(--sheet-shadow); overflow: hidden; }
  .sheet--first { left: 70px; top: 60px; width: 510px; height: 721px; }
  .sheet--follow { left: 620px; top: 222px; width: 510px; height: 360px; }

  .facet-field { position: absolute; left: 0; right: 0; background:
      linear-gradient(135deg, var(--facet-light) 0%, var(--facet-mid) 35%, var(--paper) 55%, var(--facet-deep) 80%, var(--facet-light) 100%); opacity: 0.8; }
  .sheet--first .facet-field--top { top: 0; height: 120px; }
  .sheet--follow .facet-field--top { top: 0; height: 96px; }

  .letterhead { position: absolute; right: 28px; top: 22px; text-align: right; }
  .sheet--follow .letterhead { top: 18px; }
  .letterhead__name { font-size: 15px; font-weight: 400; letter-spacing: 0.2px; }
  .letterhead__name strong { font-weight: 700; }
  .letterhead__name .divider { margin: 0 5px; }
  .letterhead__contact { font-size: 9.5px; color: var(--ink-soft); margin-top: 2px; }
  .letterhead__contact .divider { margin: 0 4px; }
  .services { display: flex; justify-content: flex-end; gap: 11px; margin-top: 9px; list-style: none; }
  .services li { font-size: 8.5px; font-weight: 600; letter-spacing: 0.4px; display: flex; align-items: center; gap: 4px; }
  .services li::before { content: ""; width: 6px; height: 6px; border-radius: 50%; background: var(--ink); }

  .letter { position: absolute; left: 48px; right: 48px; font-size: 11px; line-height: 1.45; color: var(--ink-soft); }
  .sheet--first .letter { top: 150px; }
  .sheet--follow .letter { top: 122px; font-size: 13px; }
  .letter__recipient { margin-bottom: 14px; }
  .letter__salutation { margin-bottom: 2px; }
  .letter p { margin-bottom: 10px; }
  .letter__closing { margin-top: 8px; }
  .signature { display: block; width: 110px; height: 28px; margin: 8px 0 2px;
    background: linear-gradient(90deg, #cfcfcf, #e7e7e7); border-radius: 3px; }
</style>
</head>
<body>
<main class="canvas">

  <section class="sheet sheet--first" aria-label="Briefbogen erste Seite">
    <div class="facet-field facet-field--top" role="img" aria-label="Feld aus hellgrauen, überlappenden Quadraten"></div>
    <header class="letterhead">
      <h1 class="letterhead__name"><strong>Valmor Keller</strong><span class="divider">|</span>eidg.dipl. Malermeister</h1>
      <p class="letterhead__contact">Birkenweg 7<span class="divider"> </span>8805 Seeheim<span class="divider">|</span>Telefon 044 583 61 47<span class="divider">|</span>Fax 044 583 61 37<span class="divider">|</span>gutachten@valmorkeller.example</p>
      <ul class="services">
        <li>GUTACHTEN</li><li>EXPERTISEN</li><li>DEVISIERUNGEN</li><li>FARBBERATUNGEN</li><li>DEKORATIVE</li><li>GESTALTUNGEN</li>
      </ul>
    </header>
    <article class="letter">
      <address class="letter__recipient" style="font-style:normal">November 1, 2012<br>Mr. Tomas Grey<br>56 Sample Row Lane<br>Northfield, U.K 54321</address>
      <p class="letter__salutation">Dear Mr. Grey</p>
      <p>The first paragraph of a typical business letter is used to state the main point of the letter. Begin with a friendly opening; then quickly transition into the purpose of your letter. Use a couple of sentences to explain the purpose, but do not go into detail until the next paragraph.</p>
      <p>Beginning with the second paragraph, state the supporting details to justify your purpose. These may take the form of background information, statistics or first-hand accounts. A few short paragraphs within the body of the letter should be enough to support your reasoning.</p>
      <p>Finally, in the closing paragraph, briefly restate your purpose and why it is important. If the purpose of your letter is employment related, consider ending your letter with your contact information. However, if the purpose is informational, think about closing with gratitude for the reader's time.</p>
      <p class="letter__closing">Sincerely,</p>
      <span class="signature" role="img" aria-label="Handschriftliche Unterschrift von Reid Hollis"></span>
      <p>President</p>
    </article>
  </section>

  <section class="sheet sheet--follow" aria-label="Briefbogen Folgeseite">
    <div class="facet-field facet-field--top" role="img" aria-label="Feld aus hellgrauen, überlappenden Quadraten"></div>
    <header class="letterhead">
      <h2 class="letterhead__name"><strong>Valmor Keller</strong><span class="divider">|</span>eidg.dipl. Malermeister</h2>
      <p class="letterhead__contact">Birkenweg 7<span class="divider"> </span>8805 Seeheim<span class="divider">|</span>Telefon 044 583 61 47<span class="divider">|</span>Fax 044 583 61 37</p>
      <ul class="services">
        <li>GUTACHTEN</li><li>EXPERTISEN</li><li>DEVISIERUNGEN</li><li>FARBBERATUNGEN</li><li>DEKORATIVE</li><li>GESTALTUNGEN</li>
      </ul>
    </header>
    <article class="letter">
      <address class="letter__recipient" style="font-style:normal">November 1, 2012<br>Mr. Tomas Grey<br>56 Sample Row Lane<br>Northfield, U.K 54321</address>
      <p class="letter__salutation">Dear Mr. Grey</p>
      <p>The first paragraph of a typical business letter is used to state the main point of the letter. Begin with a friendly opening; then quickly transition into the purpose of</p>
    </article>
  </section>

</main>
</body>
</html>
```